Child Care Centre needs new roadside billboard / sign*

We have a 2400mm x 1200mm sign that needs to be refreshed. The design is dated and we want to create a new cleaner, more readable roadside signIt needs to be readable from about 100m awayThe text requirements are simple, but we need it to have a warm, family feel.We are located in a small beach side community and we have a lot of bright colours in our centre (a lot of blues and yellows)https://www.saltmarshchildcare.com.au/

Target Market(s)

Parents of young children

Industry/Entity Type

Childcare

Colors
fbed22
0355a3

Requirements
Must have
• Readable from c.100m
• Simple, warm design
Should not have
• Cluttered or overly busy

```html
<!DOCTYPE html>
<html lang="en">
<head>
<meta charset="utf-8">
<title>Saltmarsh Early Education – Roadside Sign</title>
<link href="https://fonts.googleapis.com/css2?family=Arvo:wght@700&family=Montserrat:wght@800&display=swap" rel="stylesheet">
<style>
  :root {
    --page: #e4e4e4;
    --sky-top: #dff1fb;
    --sky-blush: #fbe6ea;
    --sky-low: #eef7fd;
    --pink: #e4297a;
    --purple: #ad2a8f;
    --blue: #0355a3;
    --green: #0aa04a;
    --yellow: #fbed22;
    --wave: #7fd5f6;
    --mascot: #f5ec3a;
  }
  * { margin: 0; padding: 0; box-sizing: border-box; }
  html, body {
    width: 1200px;
    height: 1200px;
    overflow: hidden;
    background: var(--page);
  }
  .sign {
    position: absolute;
    left: 0;
    top: 300px;
    width: 1200px;
    height: 600px;
    overflow: hidden;
  }
  .sky {
    position: absolute;
    inset: 0;
    background: linear-gradient(180deg, var(--sky-top) 0%, #f4f0f6 30%, var(--sky-blush) 48%, #f7f9fc 66%, var(--sky-low) 100%);
  }
  .mascot {
    position: absolute;
    left: 186px;
    top: 33px;
    width: 143px;
    height: 220px;
    border-radius: 60px 60px 40px 40px;
    background: linear-gradient(180deg, #f9f27a 0%, var(--mascot) 100%);
  }
  .brand {
    position: absolute;
    left: 330px;
    top: 26px;
    width: 720px;
    text-align: center;
    font-family: 'Arvo', serif;
    font-weight: 700;
    color: var(--blue);
    line-height: 1;
  }
  .brand-name { display: block; font-size: 112px; }
  .brand-tagline { display: block; font-size: 74px; margin-top: 8px; }
  .service {
    position: absolute;
    font-family: 'Arvo', serif;
    font-weight: 700;
    text-align: center;
    text-transform: uppercase;
    line-height: 43px;
  }
  .service-left { left: 40px; width: 500px; }
  .service-right { left: 600px; width: 552px; }
  .school-care { top: 280px; font-size: 44px; color: var(--pink); }
  .vacation-care { top: 383px; font-size: 44px; color: var(--purple); }
  .long-day { top: 271px; font-size: 42px; color: var(--blue); }
  .hours { top: 380px; font-size: 43px; color: var(--green); }
  .rule {
    position: absolute;
    height: 4px;
    background: var(--blue);
  }
  .rule-left { left: 63px; width: 454px; top: 376px; }
  .rule-right { left: 624px; width: 505px; top: 373px; }
  .wave-band {
    position: absolute;
    left: 0;
    top: 480px;
    width: 1200px;
    height: 120px;
  }
  .phone {
    position: absolute;
    left: 0;
    top: 512px;
    width: 1176px;
    text-align: center;
    font-family: 'Montserrat', sans-serif;
    font-weight: 800;
    font-size: 80px;
    letter-spacing: -1px;
    color: var(--blue);
    line-height: 1;
  }
</style>
</head>
<body>
  <main class="sign">
    <div class="sky" role="img" aria-label="Soft pastel sky background with a faint rainbow and clouds"></div>

    <div class="mascot" role="img" aria-label="Cartoon yellow seahorse mascot wearing a graduation cap and holding a diploma"></div>

    <h1 class="brand">
      <span class="brand-name">Saltmarsh</span>
      <span class="brand-tagline">Early Education</span>
    </h1>

    <p class="service service-left school-care">Before and after<br>school care</p>
    <div class="rule rule-left"></div>
    <p class="service service-left vacation-care">Vacation care</p>

    <p class="service service-right long-day">6 weeks to 6 years<br>(long day care)</p>
    <div class="rule rule-right"></div>
    <p class="service service-right hours">Open 6.30 am – 6.30 pm<br>52 weeks a year</p>

    <svg class="wave-band" viewBox="0 0 1200 120" preserveAspectRatio="none" aria-hidden="true">
      <path d="M0 30 Q23 14 46 30 T92 30 T138 30 T184 30 T230 30 T276 30 T322 30 T368 30 T414 30 T460 30 T506 30 T552 30 T598 30 T644 30 T690 30 T736 30 T782 30 T828 30 T874 30 T920 30 T966 30 T1012 30 T1058 30 T1104 30 T1150 30 T1196 30 T1242 30 L1242 120 L0 120 Z" fill="var(--yellow)"/>
      <path d="M0 30 Q23 14 46 30 T92 30 T138 30 T184 30 T230 30 T276 30 T322 30 T368 30 T414 30 T460 30 T506 30 T552 30 T598 30 T644 30 T690 30 T736 30 T782 30 T828 30 T874 30 T920 30 T966 30 T1012 30 T1058 30 T1104 30 T1150 30 T1196 30 T1242 30" fill="none" stroke="var(--wave)" stroke-width="8"/>
    </svg>

    <p class="phone">07 5550 1234</p>
  </main>
</body>
</html>
```